New Basketball Sports Agency need webpage design

We are a GRVO/PKL Sports agency looking for a new Webpage design. We currently have a site @ www.tqrhoopsgroup.example, and looking for someone to redesign the site.. We are also looking to redo the LOGO as well. TQR will begin its Vantage clinics also, and would like a page to promote and sign up for camp. I already have quidlane, but not sure how to add to site. Site must include:

Page for Agency updates, Client profiles, page for admin, camp registration page, flash photos, and able to filter news updates from contihoops, and KWVR sites.
Updates

Target Market(s)

European basketball clubs, USA Teams, Basketball Players, Sports Agents, Sports Directors General Managers,

Industry/Entity Type

News

```html
<!DOCTYPE html>
<html lang="en">
<head>
<meta charset="utf-8">
<title>TQR Tidewater Sport Management</title>
<link href="https://fonts.googleapis.com/css2?family=Oswald:wght@400;500;600&family=Open+Sans:wght@400;600;700&display=swap" rel="stylesheet">
<style>
:root{
  --red:#d9161c;
  --orange:#f7941d;
  --ink:#222;
  --text:#444;
  --muted:#888;
  --rule:#dcdcdc;
  --side:#f1f1f1;
  --night:#0d0d0d;
  --white:#fff;
}
*{box-sizing:border-box;margin:0;padding:0}
html,body{width:1200px;height:2233px;overflow:hidden}
body{background:var(--night);font-family:"Open Sans",Arial,sans-serif;color:var(--text);position:relative}
.side-photo{position:absolute;top:0;height:1150px;width:227px;background:linear-gradient(180deg,#3a3a3a 0%,#777 25%,#555 50%,#1a1a1a 85%,var(--night) 100%)}
.side-photo.left{left:0}
.side-photo.right{right:0;width:229px;background:linear-gradient(180deg,#6a6a6a 0%,#9a9a9a 20%,#4a4a4a 55%,#151515 85%,var(--night) 100%)}
.page{position:absolute;left:227px;top:0;width:744px;height:2233px;background:var(--white)}
/* header */
.brand{position:absolute;left:8px;top:8px;display:flex;align-items:center;gap:8px}
.brand-dot{width:44px;height:44px;border-radius:50%;background:var(--orange)}
.brand-name{font-family:"Oswald",sans-serif;font-weight:600;font-size:30px;color:var(--red);letter-spacing:1px}
.util{position:absolute;right:12px;top:8px;font-size:10px;color:var(--muted);display:flex;gap:16px}
.social{position:absolute;display:flex;gap:4px}
.social span{width:24px;height:24px;display:block;border-radius:3px}
.nav{position:absolute;left:4px;top:84px;width:736px;height:31px;background:var(--red);display:flex;align-items:center;padding-left:18px}
.nav a{font-family:"Oswald",sans-serif;color:var(--white);font-size:12.5px;text-decoration:none;white-space:nowrap;padding:0 18px 0 0;margin-right:18px;border-right:1px solid rgba(255,255,255,.35);line-height:14px;letter-spacing:.3px}
.nav a:last-child{border:0}
/* hero */
.hero{position:absolute;left:4px;top:119px;width:736px;height:314px;background:linear-gradient(90deg,#0b0b0b 0%,#1c1c1c 45%,#2a2a2a 70%,#111 100%);overflow:hidden}
.hero-photo{position:absolute;left:430px;top:10px;width:200px;height:300px;background:radial-gradient(ellipse at center,#6b3a2a 0%,#3a2a24 45%,rgba(30,30,30,0) 72%)}
.hero h1{position:absolute;left:26px;top:26px;font-family:"Oswald",sans-serif;font-weight:500;color:var(--white);font-size:30px;line-height:34px;letter-spacing:1px}
.hero h1 strong{display:block;color:var(--orange);font-size:50px;line-height:56px;font-weight:500}
.hero p{position:absolute;left:26px;top:120px;width:420px;font-size:11px;line-height:16px;color:#ddd}
.dots{position:absolute;left:26px;bottom:14px;display:flex;gap:5px}
.dots i{width:7px;height:7px;background:#777;display:block}
.dots i:first-child{background:var(--white)}
/* sections */
.head{display:flex;align-items:center;justify-content:space-between;border-bottom:2px solid var(--rule);padding-bottom:6px;position:relative}
.head::after{content:"";position:absolute;left:0;bottom:-2px;width:40px;height:2px;background:var(--orange)}
.head h2{font-family:"Oswald",sans-serif;font-weight:500;font-size:17px;color:var(--ink);display:flex;align-items:center;gap:8px;letter-spacing:.3px}
.head h2 span{font-weight:400;color:#555}
.head .all{font-size:9px;color:var(--muted)}
.main{position:absolute;left:4px;width:467px}
.sidebar-bg{position:absolute;left:478px;top:433px;width:262px;height:1745px;background:var(--side)}
.aside{position:absolute;left:482px;width:255px}
.ph{display:block}
/* awards */
.award-photos{display:flex;gap:12px;margin-top:20px}
.award-photos .ph{width:227px;height:139px}
.achievements{display:flex;gap:12px;margin-top:8px}
.achievements ul{list-style:none;width:227px}
.achievements li{font-size:9.5px;line-height:21px;color:var(--text);padding-left:10px;position:relative}
.achievements li::before{content:"";position:absolute;left:0;top:9px;width:4px;height:4px;background:#bbb}
/* news */
.news-item{display:flex;gap:10px;height:112px;border-bottom:1px solid #eee;padding-top:10px}
.news-item .ph{width:84px;height:86px;flex:none}
.news-item h3{font-size:11px;font-weight:700;color:var(--ink);margin-bottom:3px}
.news-item p{font-size:9.5px;line-height:14px}
.more{color:var(--red)}
/* videos */
.videos{display:grid;grid-template-columns:repeat(4,110px);column-gap:9px;row-gap:16px;margin-top:20px}
.video .ph{width:110px;height:86px;position:relative}
.play{position:absolute;right:8px;top:30px}
.video p{font-size:9px;line-height:12px;color:var(--ink);font-weight:600;margin-top:6px}
.video .meta{display:flex;justify-content:space-between;font-size:9px;color:var(--muted);margin-top:5px;font-weight:400}
/* gallery */
.gallery{display:flex;gap:7px;margin-top:18px}
.gallery .big{width:254px;height:202px}
.thumbs{display:grid;grid-template-columns:repeat(3,66px);grid-auto-rows:47px;gap:4px}
/* sidebar */
.field{display:flex;height:30px;margin-top:8px;background:var(--white);border:1px solid #ddd}
.field .ic{width:32px;background:#e4e4e4;display:flex;align-items:center;justify-content:center}
.field span{font-size:10px;color:var(--muted);padding-left:12px;line-height:28px}
.signup-btn{margin-top:14px;width:106px;height:32px;background:var(--orange);color:var(--white);font-family:"Oswald",sans-serif;font-size:16px;display:flex;align-items:center;justify-content:center;gap:6px}
.blog-item{display:flex;gap:8px;height:82px;padding-top:12px}
.blog-item .ph{width:58px;height:58px;flex:none}
.blog-item .date{font-size:8px;color:var(--muted)}
.blog-item h3{font-size:10px;color:var(--ink);font-weight:700;margin:2px 0}
.blog-item p{font-size:9px;line-height:12px}
.tabs{display:flex;height:34px}
.tab{flex:1;font-family:"Oswald",sans-serif;color:var(--white);font-size:13px;display:flex;align-items:center;justify-content:center;gap:6px}
.tab.a{background:var(--orange)}
.tab.b{background:var(--red)}
.feed-item{display:flex;gap:10px;height:68px;padding-top:12px}
.cal{width:44px;height:50px;background:var(--red);color:var(--white);text-align:center;font-family:"Oswald",sans-serif;flex:none}
.cal b{display:block;font-size:20px;line-height:28px;font-weight:500}
.cal small{font-size:12px;line-height:14px;display:block;border-top:1px solid rgba(255,255,255,.4)}
.feed-item h3{font-size:10px;color:var(--ink);font-weight:700}
.feed-item p{font-size:9px;line-height:12px}
.pro-grid{display:grid;grid-template-columns:1fr 1fr;row-gap:14px;margin-top:18px}
.pro{display:flex;gap:8px}
.pro .badge{width:40px;height:44px;flex:none;border:1px solid #ddd;background:var(--white);display:flex;align-items:center;justify-content:center}
.pro .badge i{width:22px;height:30px;display:block}
.pro h3,.link h3{font-family:"Oswald",sans-serif;font-size:13px;color:var(--ink);font-weight:500;line-height:15px}
.pro p,.link p{font-size:9px;line-height:12px}
.link{display:flex;gap:12px;align-items:center;height:58px;margin-top:6px}
.link .badge{width:76px;height:40px;flex:none;background:var(--white);border:1px solid #ddd;display:flex;align-items:center;justify-content:center}
.link .badge i{width:50px;height:22px;display:block}
.checklist{display:flex;gap:10px;align-items:center;margin-top:14px}
.checklist h3{font-family:"Oswald",sans-serif;font-size:13px;font-weight:500;color:var(--ink)}
.dl{display:inline-block;background:var(--red);color:var(--white);font-size:9px;padding:3px 8px;margin-top:3px}
/* footer */
.footer{position:absolute;left:4px;top:2196px;width:736px;height:30px;background:#161616;display:flex;align-items:center;justify-content:space-between;padding:0 12px}
.footer p{font-size:9px;color:#bbb}
</style>
</head>
<body>

<div class="side-photo left" role="img" aria-label="Black and white photo of a basketball player in a sleeveless jersey"></div>
<div class="side-photo right" role="img" aria-label="Black and white photo of a basketball player dunking"></div>

<div class="page">

  <header>
    <div class="brand"><span class="brand-dot"></span><span class="brand-name">TQR</span></div>
    <div class="util"><span>&#9993; CONTACT US</span><span>&#9638; OTHER PAGES</span></div>
    <div class="social" style="right:10px;top:32px">
      <span style="background:#3b5998"></span><span style="background:#2aa9e0"></span><span style="background:#0e76a8"></span><span style="background:#dd4b39"></span><span style="background:#12a5e8"></span><span style="background:#c4302b"></span>
    </div>
  </header>

  <nav class="nav">
    <a>HOME</a><a>CLIENTS</a><a>BASKETBALL BOOTCAMP</a><a>HIGH SCHOOL SERVICES</a><a>AGENCY UPDATES</a><a>CAMP REGISTRATION</a>
  </nav>

  <section class="hero">
    <div class="hero-photo" role="img" aria-label="Photo of a basketball player in a red jersey dribbling a ball"></div>
    <h1>TQR TIDEWATER<strong>SPORT MANAGEMENT</strong></h1>
    <p>This is a Studio version of Lorem Ipsum. Proin gravida nibh vel velit auctor aliquet. Aenean sollicitudin, lorem quis bibendum auctor, nisi elit consequat ipsum, nec sagittis sem nibh id elit. Duis sed odio sit amet nibh vulputate cursus a sit amet mauris. Morbi accumsan ipsum velit.</p>
    <div class="dots"><i></i><i></i><i></i><i></i><i></i></div>
  </section>

  <div class="sidebar-bg"></div>

  <!-- Awards -->
  <section class="main" style="top:446px">
    <div class="head"><h2><svg width="12" height="16" viewBox="0 0 12 16"><circle cx="6" cy="5" r="4.5" fill="none" stroke="#555" stroke-width="1.6"/><path d="M3 9 L2 15 L6 13 L10 15 L9 9" fill="#555"/></svg>AWARDS<span>/ACHIEVEMENTS</span></h2><span class="all">Show All &gt;&gt;</span></div>
    <div class="award-photos">
      <div class="ph" role="img" aria-label="Portrait photo of client Darnell Okafor with his college emblem" style="background:linear-gradient(90deg,#d9c89a,#a58a4e 50%,#4a2d7a)"></div>
      <div class="ph" role="img" aria-label="Portrait photo of a client in a team jersey" style="background:linear-gradient(180deg,#3a5a8a,#8a6a50 60%,#2b2b2b)"></div>
    </div>
    <div class="achievements">
      <ul>
        <li>2010-All Conference Freshman Team(Tri-South)</li>
        <li>2013-NCAC Mid-East Region 1st Team</li>
        <li>2013-All Mid-East Region 1st Team</li>
        <li>2013-K-MAC Athlete of the Week (2X)</li>
        <li>2013-Ranked K-MAC Top 5-Steals (#1)</li>
        <li>2013-Ranked K-MAC Top 10-Rebound (#8)</li>
        <li>2013-Ranked K-MAC Top 5-Scoring (#5)</li>
        <li>2013-Ranked K-MAC Top 5-Assists(#3)</li>
      </ul>
      <ul>
        <li>2010-1st Team All Region</li>
        <li>2010-All-American</li>
        <li>2010- Jucco Top 100-All-American</li>
        <li>2011- Preseason All-American</li>
        <li>2012- Nation Top Free-Throw % (96.1)</li>
        <li>2012-All ~LPC Honorable Mention</li>
        <li>2013- All WRAC Honorable Mention</li>
        <li>2013- Scored over 2,000 career points</li>
      </ul>
    </div>
  </section>

  <!-- News -->
  <section class="main" style="top:861px">
    <div class="head"><h2><svg width="16" height="14" viewBox="0 0 16 14"><rect x="1" y="1" width="14" height="12" fill="none" stroke="#555" stroke-width="1.6"/><path d="M4 5h8M4 8h8M4 11h5" stroke="#555" stroke-width="1.4"/></svg>UPCOMING <span>NEWS</span></h2><span class="all">Show All &gt;&gt;</span></div>
    <div class="news-item"><div class="ph" role="img" aria-label="Photo of point guard Darnell Okafor" style="background:linear-gradient(135deg,#c9b07a,#5a3a2a 60%,#4a2d7a)"></div><div><h3>TQR signs Brookfield's Point Guard Darnell Okafor</h3><p>Darnell is a floor-general with tremendous heart and determination...Will battle tooth and nail on every possession...Clutch performer who seems to shine when it matters most...his ability to run the team and make plays for others, as well a maintaining above a 3-to-1 ast/to ratio is enough to label him a legitimate point... <span class="more">[Readmore...]</span></p></div></div>
    <div class="news-item"><div class="ph" role="img" aria-label="Photo of shooting guard Keon Whitlow" style="background:linear-gradient(135deg,#d8a070,#6a4030 55%,#8a8a8a)"></div><div><h3>TQR lands Nations Top Freethrow Shooting PG Keon Whitlow</h3><p>Keon is an athletic undersized point guard with terrific scoring instincts... Scored 59 points against JCLC-Marlow in the championship game of The Harbor Classic his freshman season shooting 21-for-26 from the field, 9-for-9 from 3-point range and 8-for-8 from the foul line... Extremely quick and agile,amazingly good rebounder considering his size, Creates havoc on both ends of the floor... <span class="more">[Readmore...]</span></p></div></div>
    <div class="news-item"><div class="ph" role="img" aria-label="Photo of Tyrese Hallam shooting in a game" style="background:linear-gradient(135deg,#e6e6e6,#4a5a9a 55%,#c9c9c9)"></div><div><h3>Brookfield's Tyrese Hallam Joins TQR!</h3><p>The 6'2" PG/SG Tyrese Hallam just signed a representation agreement with Tidewater Sports Management. He is a product of Brookfield Wesleyan University under coach Len Carver. He's a player with definite PKL athletic potential... Uses his quickness and excellent handle to change directions and breakdown the defense.. Shines in the open floor where he attacks the basket and uses... <span class="more">[Readmore...]</span></p></div></div>
    <div class="news-item"><div class="ph" role="img" aria-label="Photo of a scouting seminar in a gym" style="background:linear-gradient(135deg,#6a5a4a,#b08a5a 50%,#3a3a3a)"></div><div><h3>Coming Soon!!! TQR Scouting Seminars for Highschool Athletes</h3><p>TQR's scouting Seminars for High School Boys/Girls is open to Division 1 scouting services, Division 2, Division 3, NIAA, JUCO and Prep School coaches from in and out of state. We will invite every D2, D3, NIAA, JUCO and prep school in the South Eastern region to attend. TQR will also be evaluating this event with the intent to distribute to colleges unable to attend... <span class="more">[Readmore...]</span></p></div></div>
    <div class="news-item" style="border:0"><div class="ph" role="img" aria-label="Portrait photo of Tyrese Hallam" style="background:linear-gradient(180deg,#d9d2c4,#7a5a44 55%,#f0f0f0)"></div><div><h3>Brookfield's Tyrese Hallam Joins TQR!</h3><p>The 6'2" PG/SG Tyrese Hallam just signed a representation agreement with Tidewater Sports Management. He is a product of Brookfield Wesleyan University under coach Len Carver. He's a player with definite PKL athletic potential... Uses his quickness and excellent handle to change directions and breakdown the defense.. Shines in the open floor where he attacks the basket and uses... <span class="more">[Readmore...]</span></p></div></div>
  </section>

  <!-- Videos -->
  <section class="main" style="top:1497px">
    <div class="head"><h2><svg width="15" height="15" viewBox="0 0 16 16"><circle cx="8" cy="8" r="7" fill="#555"/><path d="M6 4l5 4-5 4z" fill="#fff"/></svg>TOP <span>VIDEOS</span></h2><span class="all">Show All &gt;&gt;</span></div>
    <div class="videos">
      <div class="video"><div class="ph" role="img" aria-label="Video still of a basketball game" style="background:linear-gradient(135deg,#c9a27a,#b03a2a 50%,#e8e0d0)"><svg class="play" width="20" height="20" viewBox="0 0 20 20"><circle cx="10" cy="10" r="9" fill="#fff"/><path d="M8 6l4 4-4 4" fill="none" stroke="#333" stroke-width="2"/></svg></div><p>This is a Studio version of Lorem Ipsum.</p><div class="meta"><span>&#9673; 2,215</span><span>1 week Ago</span></div></div>
      <div class="video"><div class="ph" role="img" aria-label="Video still of players on an outdoor court" style="background:linear-gradient(135deg,#9ac0e0,#6a8a5a 55%,#c0a080)"><svg class="play" width="20" height="20" viewBox="0 0 20 20"><circle cx="10" cy="10" r="9" fill="#fff"/><path d="M8 6l4 4-4 4" fill="none" stroke="#333" stroke-width="2"/></svg></div><p>This is a Studio version of Lorem Ipsum.</p><div class="meta"><span>&#9673; 2,215</span><span>1 week Ago</span></div></div>
      <div class="video"><div class="ph" role="img" aria-label="Video still of players in a gym" style="background:linear-gradient(135deg,#8a7a6a,#c0b0a0 50%,#5a4a3a)"><svg class="play" width="20" height="20" viewBox="0 0 20 20"><circle cx="10" cy="10" r="9" fill="#fff"/><path d="M8 6l4 4-4 4" fill="none" stroke="#333" stroke-width="2"/></svg></div><p>This is a Studio version of Lorem Ipsum.</p><div class="meta"><span>&#9673; 2,215</span><span>1 week Ago</span></div></div>
      <div class="video"><div class="ph" role="img" aria-label="Video still of a dunk in an arena" style="background:linear-gradient(135deg,#3a3a3a,#c05030 50%,#2a2a4a)"><svg class="play" width="20" height="20" viewBox="0 0 20 20"><circle cx="10" cy="10" r="9" fill="#fff"/><path d="M8 6l4 4-4 4" fill="none" stroke="#333" stroke-width="2"/></svg></div><p>This is a Studio version of Lorem Ipsum.</p><div class="meta"><span>&#9673; 2,215</span><span>1 week Ago</span></div></div>
      <div class="video"><div class="ph" role="img" aria-label="Video still of a team huddle" style="background:linear-gradient(135deg,#e0d0b0,#2a4a8a 55%,#d0d0d0)"><svg class="play" width="20" height="20" viewBox="0 0 20 20"><circle cx="10" cy="10" r="9" fill="#fff"/><path d="M8 6l4 4-4 4" fill="none" stroke="#333" stroke-width="2"/></svg></div><p>This is a Studio version of Lorem Ipsum.</p><div class="meta"><span>&#9673; 2,215</span><span>1 week Ago</span></div></div>
      <div class="video"><div class="ph" role="img" aria-label="Video still of a layup" style="background:linear-gradient(135deg,#b0c8e0,#d08040 50%,#5a6a8a)"><svg class="play" width="20" height="20" viewBox="0 0 20 20"><circle cx="10" cy="10" r="9" fill="#fff"/><path d="M8 6l4 4-4 4" fill="none" stroke="#333" stroke-width="2"/></svg></div><p>This is a Studio version of Lorem Ipsum.</p><div class="meta"><span>&#9673; 2,215</span><span>1 week Ago</span></div></div>
      <div class="video"><div class="ph" role="img" aria-label="Video still of a camp drill" style="background:linear-gradient(135deg,#7a6a5a,#a0a0a0 50%,#3a3a3a)"><svg class="play" width="20" height="20" viewBox="0 0 20 20"><circle cx="10" cy="10" r="9" fill="#fff"/><path d="M8 6l4 4-4 4" fill="none" stroke="#333" stroke-width="2"/></svg></div><p>This is a Studio version of Lorem Ipsum.</p><div class="meta"><span>&#9673; 2,215</span><span>1 week Ago</span></div></div>
      <div class="video"><div class="ph" role="img" aria-label="Video still of a player shooting" style="background:linear-gradient(135deg,#e8e8e8,#c08a60 55%,#4a6a9a)"><svg class="play" width="20" height="20" viewBox="0 0 20 20"><circle cx="10" cy="10" r="9" fill="#fff"/><path d="M8 6l4 4-4 4" fill="none" stroke="#333" stroke-width="2"/></svg></div><p>This is a Studio version of Lorem Ipsum.</p><div class="meta"><span>&#9673; 2,215</span><span>1 week Ago</span></div></div>
    </div>
  </section>

  <!-- Gallery -->
  <section class="main" style="top:1879px">
    <div class="head"><h2><svg width="16" height="14" viewBox="0 0 16 14"><rect x="1" y="2" width="14" height="11" fill="#555"/><circle cx="8" cy="7.5" r="3" fill="#fff"/></svg>PHOTO <span>GALLERY</span></h2><span class="all">Show All &gt;&gt;</span></div>
    <div class="gallery">
      <div class="ph big" role="img" aria-label="Photo of a player holding a basketball against a light backdrop" style="background:linear-gradient(135deg,#f0f0f0,#9a9a9a 40%,#2a2a2a 70%,#c05030)"></div>
      <div class="thumbs">
        <div class="ph" role="img" aria-label="Gallery photo of a game" style="background:#8a6a4a"></div>
        <div class="ph" role="img" aria-label="Gallery photo of a player" style="background:#b04030"></div>
        <div class="ph" role="img" aria-label="Gallery photo of a team" style="background:#5a6a8a"></div>
        <div class="ph" role="img" aria-label="Gallery photo of a dunk" style="background:#c08a50"></div>
        <div class="ph" role="img" aria-label="Gallery photo of players" style="background:#3a4a7a"></div>
        <div class="ph" role="img" aria-label="Gallery photo of a huddle" style="background:#a05a3a"></div>
        <div class="ph" role="img" aria-label="Gallery photo of an arena" style="background:#6a7a5a"></div>
        <div class="ph" role="img" aria-label="Gallery photo of a camp" style="background:#d0a070"></div>
        <div class="ph" role="img" aria-label="Gallery photo of a shot" style="background:#4a5a6a"></div>
        <div class="ph" role="img" aria-label="Gallery photo of a coach" style="background:#9a7a6a"></div>
        <div class="ph" role="img" aria-label="Gallery photo of a layup" style="background:#c06a40"></div>
        <div class="ph" role="img" aria-label="Gallery photo of a bench" style="background:#5a5a5a"></div>
      </div>
    </div>
  </section>

  <!-- Sidebar: signup -->
  <section class="aside" style="top:446px">
    <div class="head"><h2><svg width="16" height="14" viewBox="0 0 16 14"><path d="M1 1h14v9H6l-4 3v-3H1z" fill="#555"/></svg>SIGNUP <span>FOR CAMP</span></h2></div>
    <div style="margin-top:12px">
      <div class="field"><span class="ic"><svg width="12" height="12" viewBox="0 0 12 12"><circle cx="6" cy="4" r="3" fill="#666"/><path d="M0 12c0-4 12-4 12 0z" fill="#666"/></svg></span><span>Enter Your First Name...</span></div>
      <div class="field"><span class="ic"><svg width="12" height="12" viewBox="0 0 12 12"><circle cx="6" cy="4" r="3" fill="#666"/><path d="M0 12c0-4 12-4 12 0z" fill="#666"/></svg></span><span>Enter Your Last Name...</span></div>
      <div class="field"><span class="ic"><svg width="12" height="12" viewBox="0 0 12 12"><circle cx="6" cy="6" r="5" fill="none" stroke="#666" stroke-width="1.6"/><circle cx="6" cy="6" r="2" fill="#666"/></svg></span><span>Enter Your Email Address...</span></div>
      <div class="field"><span class="ic"><svg width="12" height="12" viewBox="0 0 12 12"><rect x="2" y="5" width="8" height="7" fill="#666"/><path d="M4 5V3a2 2 0 0 1 4 0v2" fill="none" stroke="#666" stroke-width="1.5"/></svg></span><span>Enter Your Password...</span></div>
    </div>
    <div class="signup-btn">SIGNUP <svg width="16" height="12" viewBox="0 0 16 12"><path d="M1 1l5 5-5 5M8 1l5 5-5 5" fill="none" stroke="#fff" stroke-width="2.4"/></svg></div>
  </section>

  <!-- Sidebar: blog -->
  <section class="aside" style="top:725px">
    <div class="head"><h2><svg width="15" height="15" viewBox="0 0 16 16"><circle cx="8" cy="8" r="7" fill="none" stroke="#555" stroke-width="1.8"/><path d="M8 4v4l3 2" fill="none" stroke="#555" stroke-width="1.6"/></svg>LATEST <span>BLOG</span></h2><span class="all">Show All &gt;&gt;</span></div>
    <div class="blog-item"><div class="ph" role="img" aria-label="Blog thumbnail of a player" style="background:linear-gradient(135deg,#c03020,#6a3a2a)"></div><div><div class="date">&#9719; 28 FEBRUARY, 2013 &nbsp; &#9993; 18 COMMENTS</div><h3>Lorem Ipsum is dolor sit amet...</h3><p>This is a Studio version of Lorem Ipsum. Proin gravida nibh... <span class="more">[Readmore...]</span></p></div></div>
    <div class="blog-item"><div class="ph" role="img" aria-label="Blog thumbnail of a player" style="background:linear-gradient(135deg,#c03020,#6a3a2a)"></div><div><div class="date">&#9719; 28 FEBRUARY, 2013 &nbsp; &#9993; 18 COMMENTS</div><h3>Lorem Ipsum is dolor sit amet...</h3><p>This is a Studio version of Lorem Ipsum. Proin gravida nibh... <span class="more">[Readmore...]</span></p></div></div>
    <div class="blog-item"><div class="ph" role="img" aria-label="Blog thumbnail of a player" style="background:linear-gradient(135deg,#c03020,#6a3a2a)"></div><div><div class="date">&#9719; 28 FEBRUARY, 2013 &nbsp; &#9993; 18 COMMENTS</div><h3>Lorem Ipsum is dolor sit amet...</h3><p>This is a Studio version of Lorem Ipsum. Proin gravida nibh... <span class="more">[Readmore...]</span></p></div></div>
    <div class="blog-item"><div class="ph" role="img" aria-label="Blog thumbnail of a player" style="background:linear-gradient(135deg,#c03020,#6a3a2a)"></div><div><div class="date">&#9719; 28 FEBRUARY, 2013 &nbsp; &#9993; 18 COMMENTS</div><h3>Lorem Ipsum is dolor sit amet...</h3><p>This is a Studio version of Lorem Ipsum. Proin gravida nibh... <span class="more">[Readmore...]</span></p></div></div>
  </section>

  <!-- Sidebar: feeds -->
  <section class="aside" style="top:1125px">
    <div class="tabs"><div class="tab a">&#9679; CONTIHOOPS NEWS</div><div class="tab b">&#9679; KWVR NEWS</div></div>
    <div class="feed-item"><div class="cal"><b>25</b><small>MAR</small></div><div><h3>Lorem Ipsum is dolor sit amet...</h3><p>This is a Studio version of Lorem Ipsum. Proin gravida nibh... <span class="more">[Readmore...]</span></p></div></div>
    <div class="feed-item"><div class="cal"><b>25</b><small>MAR</small></div><div><h3>Lorem Ipsum is dolor sit amet...</h3><p>This is a Studio version of Lorem Ipsum. Proin gravida nibh... <span class="more">[Readmore...]</span></p></div></div>
    <div class="feed-item"><div class="cal"><b>25</b><small>MAR</small></div><div><h3>Lorem Ipsum is dolor sit amet...</h3><p>This is a Studio version of Lorem Ipsum. Proin gravida nibh... <span class="more">[Readmore...]</span></p></div></div>
    <div class="feed-item"><div class="cal"><b>25</b><small>MAR</small></div><div><h3>Lorem Ipsum is dolor sit amet...</h3><p>This is a Studio version of Lorem Ipsum. Proin gravida nibh... <span class="more">[Readmore...]</span></p></div></div>
  </section>

  <!-- Sidebar: pro links -->
  <section class="aside" style="top:1470px">
    <div class="head"><h2><svg width="16" height="16" viewBox="0 0 16 16"><path d="M6 10l4-4M5 7L3 9a2.5 2.5 0 0 0 4 4l2-2M11 9l2-2a2.5 2.5 0 0 0-4-4L7 5" fill="none" stroke="#555" stroke-width="1.8"/></svg>PRO <span>BASKETBALL LINKS</span></h2></div>
    <div class="pro-grid">
      <div class="pro"><div class="badge"><i style="background:#1d428a"></i></div><div><h3>PKL</h3><p>League, Team,<br>Player info...</p></div></div>
      <div class="pro"><div class="badge"><i style="background:#c8102e"></i></div><div><h3>PDL</h3><p>PKL Developmental<br>League</p></div></div>
      <div class="pro"><div class="badge"><i style="background:#222"></i></div><div><h3>GRVO</h3><p>International<br>Basketball<br>Agents / players</p></div></div>
      <div class="pro"><div class="badge"><i style="background:#b01c20"></i></div><div><h3>UHA</h3><p>Universal<br>Hoops<br>Association</p></div></div>
    </div>
  </section>

  <!-- Sidebar: misc links -->
  <section class="aside" style="top:1696px">
    <div class="head"><h2><svg width="16" height="16" viewBox="0 0 16 16"><path d="M6 10l4-4M5 7L3 9a2.5 2.5 0 0 0 4 4l2-2M11 9l2-2a2.5 2.5 0 0 0-4-4L7 5" fill="none" stroke="#555" stroke-width="1.8"/></svg>MISC <span>BASKETBALL LINKS</span></h2></div>
    <div style="margin-top:8px">
      <div class="link"><div class="badge"><i style="background:#3a6ab0"></i></div><div><h3>HOOPLINE</h3><p>Guide for Youth Basketball<br>Coaches, Players, Parents</p></div></div>
      <div class="link"><div class="badge"><i style="background:#333;width:24px;height:30px"></i></div><div><h3>LEAP GUIDE</h3><p>The Most Comprehensive Vertical<br>Jump Program Available</p></div></div>
      <div class="link"><div class="badge"><i style="background:#e0701a;border-radius:50%;width:30px;height:30px"></i></div><div><h3>CONTIHOOPS</h3><p>Worldwide Basketball News<br>Players, Agents, Teams</p></div></div>
    </div>
  </section>

  <!-- Sidebar: college links -->
  <section class="aside" style="top:1956px">
    <div class="head"><h2><svg width="16" height="16" viewBox="0 0 16 16"><path d="M6 10l4-4M5 7L3 9a2.5 2.5 0 0 0 4 4l2-2M11 9l2-2a2.5 2.5 0 0 0-4-4L7 5" fill="none" stroke="#555" stroke-width="1.8"/></svg>CALA <span>BASKETBALL LINKS</span></h2></div>
    <div style="margin-top:8px">
      <div class="link"><div class="badge"><i style="background:#1d4f9a;border-radius:50%;width:30px;height:30px"></i></div><div><h3>CALA</h3><p>Eligibility, Academics, Resources</p></div></div>
      <div class="link"><div class="badge"><i style="background:#2a6a9a"></i></div><div><h3>LEAP GUIDE</h3><p>The Most Comprehensive Vertical<br>Jump Program Available</p></div></div>
    </div>
    <div class="checklist">
      <svg width="26" height="32" viewBox="0 0 26 32"><path d="M2 1h15l7 7v23H2z" fill="#fff" stroke="#c8102e" stroke-width="2"/><path d="M17 1v7h7" fill="none" stroke="#c8102e" stroke-width="2"/><path d="M7 16h12M7 21h12M7 26h8" stroke="#c8102e" stroke-width="1.6"/></svg>
      <div><h3>CHECKLIST FOR ELIGIBILITY.PDF</h3><span class="dl">Download File</span></div>
    </div>
  </section>

  <footer class="footer">
    <p>Copyright &copy; 2013 www.tqrhoopsgroup.example. All rights reserved.</p>
    <div class="social" style="position:static">
      <span style="background:#3b5998;width:18px;height:18px"></span><span style="background:#2aa9e0;width:18px;height:18px"></span><span style="background:#0e76a8;width:18px;height:18px"></span><span style="background:#dd4b39;width:18px;height:18px"></span><span style="background:#12a5e8;width:18px;height:18px"></span><span style="background:#c4302b;width:18px;height:18px"></span>
    </div>
  </footer>

</div>
</body>
</html>
```